Kestrel Vale - Multifamily Development

Kestrel Vale is a Luxury Multifamily Development project located in Orange, NJ. This project will be completed in three phases with the first phase about 75% complete. Each phase will have a different name as follows
ALDER Kestrel Vale
WILLOW Kestrel Vale
JUNIPERS Kestrel Vale
We are going to install a banner on the side of the first building which will act as advertising for all buildings. We will eventually need advertising that will be in the windows as well as marketing materials . We want the marketing for this project to be similar for all three phases. At the moment, we are starting with this first simple banner. Attached is a rough idea of the look as well as our color palette. If you feel the color palette is a little too monochrome, feel free to propose an accent color. You can also visit our website to see more info on our company as well as the project. www.tarnvx.com Finally, if you need AI files (ie. for the logo), we can send to you. Thanks..

```html
<!DOCTYPE html>
<html lang="en">
<head>
<meta charset="utf-8">
<title>Kestrel Vale – Banner</title>
<link href="https://fonts.googleapis.com/css2?family=Montserrat:wght@700&display=swap" rel="stylesheet">
<style>
  :root {
    --banner-dark: #2b2728;
    --phone-panel: #47454f;
    --paper: #ffffff;
    --ink: #ffffff;
    --logo-ink: #2b2728;
    --sky-top: #4a4a52;
    --sky-mid: #6f7a8a;
    --brick: #8a6a52;
    --street: #3c3a3a;
  }
  html, body {
    margin: 0;
    padding: 0;
    width: 927px;
    height: 1200px;
    overflow: hidden;
    background: var(--paper);
  }
  .canvas {
    position: relative;
    width: 927px;
    height: 1200px;
    font-family: "Montserrat", Arial, sans-serif;
    font-weight: 700;
  }
  .banner {
    position: absolute;
    left: 333px;
    top: 106px;
    width: 254px;
    height: 974px;
    background: var(--banner-dark);
    color: var(--ink);
    text-align: center;
  }
  .logo-box {
    position: absolute;
    left: 14px;
    top: 15px;
    width: 227px;
    height: 160px;
    background: var(--paper);
    display: flex;
    flex-direction: column;
    align-items: center;
    justify-content: center;
    color: var(--logo-ink);
  }
  .logo-name {
    font-size: 40px;
    line-height: 1;
    letter-spacing: -0.5px;
  }
  .logo-sub {
    font-size: 10.5px;
    letter-spacing: 5px;
    margin-top: 6px;
    margin-right: -5px;
  }
  .project-name {
    position: absolute;
    left: 0;
    top: 198px;
    width: 100%;
    margin: 0;
    font-size: 31px;
    line-height: 44px;
    letter-spacing: 0.5px;
  }
  .phone {
    position: absolute;
    left: 13px;
    top: 309px;
    width: 228px;
    height: 39px;
    background: var(--phone-panel);
    font-size: 27px;
    line-height: 39px;
  }
  .hero {
    position: absolute;
    left: 0;
    top: 348px;
    width: 254px;
    height: 413px;
    background: linear-gradient(180deg, var(--sky-top) 0%, var(--sky-mid) 22%, var(--brick) 40%, var(--brick) 82%, var(--street) 100%);
  }
  .tagline {
    position: absolute;
    left: 0;
    top: 776px;
    width: 100%;
    margin: 0;
    font-size: 26px;
    line-height: 39px;
  }
  .rule {
    position: absolute;
    left: 18px;
    top: 915px;
    width: 219px;
    height: 2px;
    background: var(--ink);
  }
  .website {
    position: absolute;
    left: 0;
    top: 926px;
    width: 100%;
    font-size: 29px;
    line-height: 36px;
  }
</style>
</head>
<body>
  <div class="canvas">
    <section class="banner">
      <div class="logo-box">
        <span class="logo-name">TARN</span>
        <span class="logo-sub">PROPERTIES</span>
      </div>
      <h1 class="project-name">KESTREL<br>VALE</h1>
      <div class="phone">973-555-0142</div>
      <div class="hero" role="img" aria-label="Architectural rendering of the brick and grey-panel apartment building at a street corner with traffic lights, trees, pedestrians and a passing car"></div>
      <p class="tagline">LUXURY<br>APPARTMENT<br>RENTALS</p>
      <div class="rule"></div>
      <div class="website">TARNVX.COM</div>
    </section>
  </div>
</body>
</html>
```